Business Card Design Project

This is a new division in our company. "Meridale Wellsite & Safety" This is a Oilfield Safety company. I have included our new logo. I also have given our other business card. We love double sided with lots of color. We like to stand out. Please DO NOT duplicate our other card and bring your design into it. See all attached files.
Reason: forgot to change this when I posted it.
Here is the correct information card.
www.meridalewellsitesafety.com
Dwayne@meridalewellsitesafety.com
Reason: revision for a few.
Reason: was traveling and need to review designs.
Oil and Gas industry. Masculine look.
Business

```html
<!DOCTYPE html>
<html lang="en">
<head>
<meta charset="utf-8">
<title>Meridale Wellsite &amp; Safety – Business Card</title>
<link href="https://fonts.googleapis.com/css2?family=Lato:wght@400;700;900&display=swap" rel="stylesheet">
<style>
  :root {
    --stage: #e8e5e0;
    --card-dark: #0e0e0e;
    --card-light: #ffffff;
    --teal: #34bdb6;
    --orange: #f05a28;
    --green: #3aa84a;
    --shadow: rgba(0,0,0,0.18);
  }
  * { margin: 0; padding: 0; box-sizing: border-box; }
  html, body {
    width: 1200px; height: 1000px; overflow: hidden;
    background: var(--stage);
    font-family: "Lato", Arial, sans-serif;
  }
  .canvas { position: relative; width: 1200px; height: 1000px; }

  .card {
    position: absolute; left: 220px;
    width: 760px; height: 434px;
    border-radius: 22px;
    box-shadow: 0 10px 28px var(--shadow);
    overflow: hidden;
    text-align: center;
  }
  .card--back { top: 50px; background: var(--card-dark); }
  .card--front { top: 516px; background: var(--card-light); }

  .brand {
    display: flex; align-items: center; justify-content: center; gap: 22px;
  }
  .brand__mark {
    width: 58px; height: 58px; background: var(--orange); flex: none;
  }
  .brand__name {
    color: var(--teal); font-weight: 900; text-transform: uppercase;
    text-align: left; line-height: 1.02; letter-spacing: 1px;
  }

  .card--back .brand { margin-top: 112px; }
  .card--back .brand__name { font-size: 50px; }
  .tagline {
    margin-top: 22px; color: var(--teal);
    font-weight: 900; font-size: 24px; letter-spacing: 0.5px;
  }
  .website {
    position: absolute; left: 0; right: 0; bottom: 70px;
    color: var(--orange); font-weight: 700; font-size: 24px; letter-spacing: 0.5px;
  }

  .card--front .brand { margin-top: 48px; }
  .card--front .brand__mark { width: 46px; height: 46px; }
  .card--front .brand__name { font-size: 40px; }
  .person__name {
    margin-top: 28px; color: var(--teal);
    font-size: 30px; font-weight: 700; letter-spacing: 2px;
  }
  .person__role { color: var(--orange); font-size: 19px; margin-top: 2px; }

  .contact { margin-top: 24px; list-style: none; color: var(--teal); font-size: 21px; line-height: 1.24; }
  .contact__label { color: var(--green); font-weight: 700; }

  .stripes { position: absolute; left: 0; right: 0; bottom: 0; }
  .stripes__orange { height: 8px; background: var(--orange); }
  .stripes__gap { height: 6px; }
  .stripes__teal { height: 22px; background: var(--teal); }
</style>
</head>
<body>
<main class="canvas">

  <section class="card card--back" aria-label="Card back">
    <div class="brand">
      <span class="brand__mark"></span>
      <span class="brand__name">Meridale<br>Wellsite &amp; Safety</span>
    </div>
    <p class="tagline">FOR ALL YOUR ON-SITE SAFETY NEEDS</p>
    <p class="website">www.meridalewellsitesafety.com</p>
  </section>

  <section class="card card--front" aria-label="Card front">
    <div class="brand">
      <span class="brand__mark"></span>
      <span class="brand__name">Meridale<br>Wellsite &amp; Safety</span>
    </div>
    <h1 class="person__name">DWAYNE HARLAN</h1>
    <p class="person__role">Partner</p>
    <ul class="contact">
      <li><span class="contact__label">P:</span> 281-555-0142</li>
      <li><span class="contact__label">F:</span> 1-888-555-0176</li>
      <li><span class="contact__label">M:</span> 713-555-0188</li>
      <li><span class="contact__label">E:</span> Dwayne@meridalewellsitesafety.com</li>
      <li><span class="contact__label">A:</span> 4810 Ridge Creek Rd, Conroe, TX 77301</li>
    </ul>
    <div class="stripes">
      <div class="stripes__orange"></div>
      <div class="stripes__gap"></div>
      <div class="stripes__teal"></div>
    </div>
  </section>

</main>
</body>
</html>
```